Popular Australian based wellbeing and high performance podcast needs a design

I need a new, fresh design for my Keep Rising Daily podcast image. This podcast helps and enables its listeners to do their life even better by enhancing their wellbeing, mindset, happiness and leadership. I would love to see designs that include the colour blue. The final design should communicate optimism, hope, approachability and credibility.

Target Market(s)

Target is teenagers to adults wanting to enhance their wellbeing, mindset and happiness.

Font styles to use
Other font styles liked:
• Proba Pro

Colors
33a6d7
0592cd
ffffff

Requirements
Must have
• Must include: Keep Rising Daily podcast
Nice to have
• Could include: with Mick Talvero.

```html
<!DOCTYPE html>
<html lang="en">
<head>
<meta charset="utf-8">
<title>Keep Rising Daily — Podcast Cover</title>
<link rel="stylesheet" href="https://fonts.googleapis.com/css2?family=Lato:wght@400&display=swap">
<style>
  :root {
    --blue: #2ba3d8;
    --blue-deep: #0592cd;
    --paper: #eff7fa;
    --white: #ffffff;
  }
  html, body {
    margin: 0;
    padding: 0;
    width: 1200px;
    height: 1200px;
    overflow: hidden;
    background: var(--paper);
  }
  .cover {
    position: relative;
    width: 1200px;
    height: 1200px;
    overflow: hidden;
    background: var(--paper);
    font-family: "Lato", "Helvetica Neue", Arial, sans-serif;
  }
  .cover__shapes {
    position: absolute;
    inset: 0;
  }
  .cover__rule {
    position: absolute;
    left: 1102px;
    top: 0;
    width: 3px;
    height: 282px;
    background: var(--white);
  }
  .cover__web {
    position: absolute;
    left: 1104px;
    top: 508px;
    transform: translate(-50%, -50%) rotate(-90deg);
    color: var(--white);
    font-size: 24px;
    letter-spacing: 5px;
    white-space: nowrap;
  }
  .cover__title {
    position: absolute;
    left: 34px;
    top: 872px;
    margin: 0;
    color: var(--white);
    font-weight: 400;
    font-size: 128px;
    line-height: 100px;
    letter-spacing: -3px;
    text-transform: uppercase;
    white-space: nowrap;
  }
  .cover__title span { display: block; }
  .host {
    position: absolute;
    right: 56px;
    top: 982px;
    display: flex;
    flex-direction: column;
    align-items: center;
  }
  .host__mark {
    width: 102px;
    height: 102px;
    border-radius: 22px;
    background: var(--blue-deep);
  }
  .host__name {
    margin-top: 14px;
    color: var(--blue-deep);
    font-size: 60px;
    line-height: 1;
    white-space: nowrap;
  }
</style>
</head>
<body>
  <main class="cover">
    <svg class="cover__shapes" width="1200" height="1200" viewBox="0 0 1200 1200">
      <defs>
        <linearGradient id="photoTone" x1="0" y1="0" x2="1" y2="1">
          <stop offset="0" stop-color="#cfc3b5"/>
          <stop offset="0.45" stop-color="#bfb3a6"/>
          <stop offset="0.75" stop-color="#a7b0b8"/>
          <stop offset="1" stop-color="#3a3a40"/>
        </linearGradient>
      </defs>
      <polygon class="band band--top" points="0,0 1200,0 1200,972 0,12" fill="var(--blue)"/>
      <polygon class="band band--bottom" points="0,592 736,1200 0,1200" fill="var(--blue)"/>
      <circle class="portrait-ring" cx="592" cy="512" r="425" fill="none" stroke="var(--blue)" stroke-width="3"/>
      <circle class="portrait" cx="600" cy="500" r="412" fill="url(#photoTone)"
              role="img" aria-label="Portrait photo of the host smiling, seated on stone steps of a sandstone building"/>
    </svg>

    <div class="cover__rule"></div>
    <div class="cover__web">www.website.com</div>

    <h1 class="cover__title">
      <span>Keep</span>
      <span>Rising</span>
      <span>Daily</span>
    </h1>

    <div class="host">
      <div class="host__mark"></div>
      <div class="host__name">Mick Talvero</div>
    </div>
  </main>
</body>
</html>
```